Nightclub-type Event Poster Advertisement

Lumora Events is based in Christchurch, New Zealand and we have our next party coming up. We like a different flair for each of our events so are looking for some help from you guys. We are very flexible with everything - colours, layout, backgrounds, fonts, etc so it's ALL up to you. Attached is our company logo and the flyer (and poster) we used for our last party. Our website is lumoranz.example where you can find and use our photos and find more info about us if you desire.
Designs we are wanting: An A3 poster,an A6 flyer (smaller version of the poster is probably fine), tickets (140x68 mm). It would be great if a 5 mm bleed was included so we could get them printed directly.
Details for the event to be advertised are as followed:
Party Name: (TBD... will update ASAP)
05/07/2014
10pm-close
Lineup: 'Bazzo (Akl)', 'DJ Glimtrax', 'DJ's Morquent & Pelnavo', 'Quiet Harbour Pulse'.
Dorrin Hattles Central, Corner Fenwick & Oberly Streets
$10 Tickets
R18
Tickets & Enquiries: Marta on 0219047362
Presented by Lumora Entertainment
Thanks to everyone who reads this and please give it a go! Any questions don't hesitate to ask.
Target Market(s)
New Zealand Europeans in Christchurch, New Zealand between 18 and 25 years old.
Industry/Entity Type
Events
Look and feel

```html
<!DOCTYPE html>
<html lang="en">
<head>
<meta charset="utf-8">
<title>TBD – Lumora Entertainment</title>
<link rel="stylesheet" href="https://fonts.googleapis.com/css2?family=Sniglet:wght@800&family=Teko:wght@500;600&display=swap">
<style>
  :root {
    --night: #2b2b2b;
    --black: #000000;
    --white: #ffffff;
    --title-yellow: #fff04a;
    --title-edge: #c2188f;
    --date-yellow: #ffe81a;
    --venue-cream: #fff6a8;
    --burst-core: #ffd9a0;
    --burst-gold: #f7b51c;
    --burst-red: #b8102a;
    --burst-pink: #d6509e;
  }
  * { margin: 0; padding: 0; box-sizing: border-box; }
  html, body { width: 849px; height: 1200px; overflow: hidden; background: var(--black); }
  .poster {
    position: relative;
    width: 849px;
    height: 1200px;
    overflow: hidden;
    background: var(--night);
    font-family: "Teko", "Arial Narrow", sans-serif;
    color: var(--white);
  }
  .burst-art {
    position: absolute;
    inset: 0;
    background:
      radial-gradient(ellipse 520px 420px at 425px 720px,
        var(--burst-core) 0%,
        var(--burst-gold) 28%,
        var(--burst-red) 55%,
        var(--burst-pink) 72%,
        rgba(43,43,43,0) 100%);
  }
  .crowd-art {
    position: absolute;
    left: 0; right: 0;
    top: 880px; bottom: 0;
    background: linear-gradient(to bottom, rgba(0,0,0,0) 0%, var(--black) 28%, var(--black) 100%);
  }
  .title {
    position: absolute;
    left: 84px; top: 60px;
    font-family: "Sniglet", "Arial Rounded MT Bold", sans-serif;
    font-weight: 800;
    font-size: 190px;
    line-height: 1;
    letter-spacing: 4px;
    color: var(--title-yellow);
    -webkit-text-stroke: 3px var(--title-edge);
  }
  .brand {
    position: absolute;
    font-family: "Teko", "Arial Narrow", sans-serif;
    font-weight: 500;
    color: var(--white);
    text-align: center;
    line-height: 0.9;
  }
  .brand--top { right: 30px; top: 70px; width: 110px; font-size: 34px; }
  .brand--bottom { right: 12px; top: 1085px; width: 90px; font-size: 28px; }
  .date {
    position: absolute;
    left: 0; right: 0; top: 282px;
    text-align: center;
    font-weight: 500;
    font-size: 34px;
    color: var(--date-yellow);
    letter-spacing: 1px;
  }
  .lineup, .venue {
    position: absolute;
    left: 0; right: 0;
    text-align: center;
    list-style: none;
    text-transform: uppercase;
    font-weight: 600;
    text-shadow:
      -3px -3px 0 var(--black), 3px -3px 0 var(--black),
      -3px 3px 0 var(--black), 3px 3px 0 var(--black),
      0 -3px 0 var(--black), 0 3px 0 var(--black),
      -3px 0 0 var(--black), 3px 0 0 var(--black);
  }
  .lineup { top: 365px; font-size: 58px; line-height: 80px; color: var(--white); letter-spacing: 1px; }
  .venue { top: 622px; font-size: 44px; line-height: 83px; color: var(--venue-cream); }
  .details {
    position: absolute;
    left: 28px; right: 100px; top: 1116px;
    font-weight: 500;
    font-size: 22px;
    line-height: 28px;
    text-transform: uppercase;
    letter-spacing: 0.5px;
  }
  .details__row { display: flex; gap: 28px; }
  .details__row--split { justify-content: space-between; gap: 0; }
</style>
</head>
<body>
<main class="poster">
  <div class="burst-art" role="img" aria-label="Radiating stage light burst in gold, red and pink"></div>
  <div class="crowd-art" role="img" aria-label="Silhouetted party crowd with raised hands"></div>

  <h1 class="title">TBD</h1>
  <div class="brand brand--top">Lumora Events</div>

  <p class="date">05/07/2014</p>

  <ul class="lineup">
    <li>Bazzo (Akl)</li>
    <li>DJ Glimtrax</li>
    <li>DJ's Morquent &amp; Pelnavo</li>
  </ul>

  <ul class="venue">
    <li>Quiet Harbour Pulse</li>
    <li>Dorrin Hattles Central</li>
    <li>Corner Fenwick &amp; Oberly Streets</li>
  </ul>

  <div class="details">
    <div class="details__row"><span>R18</span><span>$10 Tickets</span><span>10pm-close</span></div>
    <div class="details__row details__row--split"><span>Tickets &amp; Enquiries: Marta on 0219047362</span><span>Presented by Lumora Entertainment</span></div>
  </div>

  <div class="brand brand--bottom">Lumora Events</div>
</main>
</body>
</html>
```